Hack my website! Blue Harbor needs a site

We hack stuff. No joke, that is what we do, but we are the good guys!

We do security consulting, specifically offensive security. The technical term is "Penetration Testing", but you probably know it as "hacking". Companies hire us to break in before the bad guys do. (I have a very cool job :) ).

I need a web site to describe our offerings and connect with clients.

I've included my business card and logo so you can understand what I'm looking for on the website and the color scheme.

Tag line:
Offensive Services from Offensive Minds

Target Market(s)

Medium to large businesses

Industry/Entity Type

Computer Security

Coding

Coded - Design and coding required

Number of Pages Required

2 page

Font styles to use
Sans Serif

Colors

Designer to choose colors to be used in the design.

Requirements
Must have
• Flat, clean, professional look
Nice to have
• Bonus for bootstrap. See the uploaded logo for the current colors. I'd really like this to look decent on a phone too.
Should not have
• 1. Black background
• 2. The business card is to show the colors and theme so far. Please, do NOT just slam that into the middle of the site since it doesn't make sense. It feels odd that I have to say that, but I've received multiple submissions where people have done this.

```html
<!DOCTYPE html>
<html lang="en">
<head>
<meta charset="utf-8">
<title>Blue Harbor – Offensive Security</title>
<link href="https://fonts.googleapis.com/css2?family=Open+Sans:ital,wght@0,400;0,600;0,700;1,400&family=Exo+2:ital,wght@1,500&display=swap" rel="stylesheet">
<style>
:root{
  --red:#e8414a;
  --red-dark:#c9323a;
  --ink:#1c1c1c;
  --text:#555;
  --muted:#8a8a8a;
  --paper:#ffffff;
  --mist:#efefef;
  --line:#d9d9d9;
  --night:#0b0b0b;
}
*{box-sizing:border-box;margin:0;padding:0}
html,body{width:1200px;height:3838px;overflow:hidden}
body{position:relative;background:var(--paper);font-family:"Open Sans",Arial,sans-serif;color:var(--text)}
.abs{position:absolute}
svg{display:block}

/* header */
.brand{left:77px;top:28px;display:flex;align-items:center;gap:14px}
.brand-mark{width:36px;height:36px;background:var(--red)}
.brand-name{font-size:34px;font-weight:700;letter-spacing:6px;color:var(--red)}
.call{right:80px;top:26px;display:flex;gap:14px;align-items:center}
.call-label{font-size:15px;font-weight:600;color:#333}
.call-number{font-size:24px;font-weight:700;color:var(--red)}

.nav{left:0;top:102px;width:1200px;height:64px;background:var(--red)}
.nav ul{list-style:none;display:flex;position:absolute;left:77px;top:0;height:64px}
.nav li{color:#fff;font-size:15px;line-height:64px;padding:0 22px}
.nav li.active{background:var(--ink);padding:0 40px}
.search{position:absolute;left:824px;top:10px;width:296px;height:44px;background:#fff;display:flex;align-items:center;justify-content:space-between;padding:0 16px;font-size:14px;color:#444}

/* hero */
.hero{left:0;top:166px;width:1200px;height:512px;background:linear-gradient(100deg,#15202e 0%,#1f3148 45%,#2a4766 70%,#10192a 100%)}
.hero-title{left:77px;top:300px;color:#fff;font-size:46px;line-height:66px}
.hero-title b{font-weight:700;display:block}
.hero-title span{font-weight:400}
.btn{display:inline-flex;align-items:center;justify-content:center;font-size:19px;color:#fff;text-transform:uppercase;background:var(--red)}
.btn-ghost{background:transparent;border:2px solid var(--red);color:var(--red)}
.slide-arrow{width:44px;height:36px;background:var(--red);display:flex;align-items:center;justify-content:center}

/* section titles */
.eyebrow{width:1200px;left:0;text-align:center;font-size:17px;color:#444}
.section-title{width:1200px;left:0;display:flex;justify-content:center;align-items:center;gap:14px;font-size:43px;font-weight:400;color:var(--ink);text-transform:uppercase}
.section-title .accent{color:var(--red)}
.title-mark{width:30px;height:34px;background:var(--red)}
.lead{left:160px;width:880px;text-align:center;font-size:14px;line-height:29px;color:#555}

/* services */
.services{left:0;top:1087px;width:1200px;height:1522px;background:var(--mist)}
.card-photo{width:501px;height:269px}
.card-label{width:428px;height:112px;background:#fff;box-shadow:0 3px 8px rgba(0,0,0,.18);display:flex;align-items:center;justify-content:center;text-align:center;font-size:17px;line-height:31px;color:#333;text-transform:uppercase}
.card-label.featured{background:var(--red);color:#fff}
.tagline{left:0;width:1200px;text-align:center;font-family:"Exo 2",Arial,sans-serif;font-style:italic;font-weight:500;font-size:23px;color:#333}

/* testimonials */
.testimonials{left:0;top:2609px;width:1200px;height:276px;background:var(--red);color:#fff}
.quote-badge{width:118px;height:118px;border-radius:50%;background:#fff;display:flex;align-items:center;justify-content:center;font-size:72px;font-weight:700;color:var(--ink);line-height:1}
.avatar{width:96px;height:96px;border-radius:50%;border:4px solid #fff}
.quote-text{left:294px;top:2730px;width:800px;font-size:14px;line-height:30px;font-style:italic}
.client{right:172px;top:2797px;font-size:23px}

/* contact */
.contact-photo{left:0;top:2980px;width:486px;height:422px}
.field{height:52px;background:#fff;border:1px solid var(--line);display:flex;align-items:center;justify-content:space-between;padding:0 16px;font-size:13px;color:#777}

/* call band */
.call-band{left:0;top:3402px;width:1200px;height:184px;background:var(--red);color:#fff}
.phone-circle{width:68px;height:68px;border-radius:50%;background:#fff;display:flex;align-items:center;justify-content:center}

/* footer */
.footer{left:0;top:3586px;width:1200px;height:252px;background:var(--night);color:#fff}
.footer-nav{position:absolute;left:77px;top:26px;display:flex;list-style:none}
.footer-nav li{font-size:15px;line-height:46px;padding:0 17px}
.footer-nav li.active{background:var(--red);padding:0 24px}
.social{position:absolute;top:26px;width:44px;height:44px;background:var(--red)}
.footer-heading{position:absolute;left:77px;top:114px;font-size:20px;color:var(--red)}
.info-icon{position:absolute;top:150px;width:50px;height:50px;background:var(--red);display:flex;align-items:center;justify-content:center}
.info-text{position:absolute;font-size:15px;line-height:25px}
</style>
</head>
<body>

<!-- header -->
<div class="abs brand"><div class="brand-mark"></div><div class="brand-name">BLUE HARBOR</div></div>
<div class="abs call">
  <svg width="46" height="46" viewBox="0 0 24 24"><path fill="#e8414a" d="M6.6 10.8a15.5 15.5 0 0 0 6.6 6.6l2.2-2.2c.3-.3.7-.4 1-.2 1.1.4 2.3.6 3.6.6.6 0 1 .4 1 1V20c0 .6-.4 1-1 1A17 17 0 0 1 3 4c0-.6.4-1 1-1h3.5c.6 0 1 .4 1 1 0 1.3.2 2.5.6 3.6.1.3 0 .7-.2 1z"/></svg>
  <div><div class="call-label">Call Us Today :</div><div class="call-number">555 - 014 - 2290</div></div>
</div>

<nav class="abs nav">
  <ul><li class="active">HOME</li><li>ABOUT US</li><li>SERVICES</li><li>NEWS</li><li>CONTACT US</li></ul>
  <div class="search">Search...
    <svg width="20" height="20" viewBox="0 0 24 24"><circle cx="10" cy="10" r="7" fill="none" stroke="#222" stroke-width="3"/><path d="M15 15l6 6" stroke="#222" stroke-width="3"/></svg>
  </div>
</nav>

<!-- hero -->
<div class="abs hero" role="img" aria-label="Businessman in a suit holding a glowing cloud icon between his hands"></div>
<div class="abs hero-title"><b>OFFENSIVE SOLUTIONS FROM</b><span>OFFENSIVE MINDS</span></div>
<div class="abs btn btn-ghost" style="left:77px;top:450px;width:186px;height:62px">Learn More</div>
<div class="abs btn" style="left:276px;top:450px;width:186px;height:62px">Contact Us</div>
<div class="abs slide-arrow" style="left:10px;top:388px"><svg width="14" height="18" viewBox="0 0 14 18"><path d="M11 2L3 9l8 7" fill="#fff"/></svg></div>
<div class="abs slide-arrow" style="right:10px;top:388px"><svg width="14" height="18" viewBox="0 0 14 18"><path d="M3 2l8 7-8 7" fill="#fff"/></svg></div>

<!-- welcome -->
<h1 class="abs section-title" style="top:732px"><span class="title-mark"></span><span><span class="accent">Welcome to</span> Blue Harbor</span></h1>
<p class="abs lead" style="top:802px">Red Team Adversary Simulation - A goal based assessment where we attack just like a real world adversary. This includes external attacks and targeted phishing to demonstrate the real risk to your data.</p>
<p class="abs lead" style="top:862px">Lorem Ipsum is simply dummy text of the printing and typesetting industry. Lorem Ipsum has been the industry's standard dummy text ever since the 1500s, when an unknown printer took a galley of type and scrambled it to make a type specimen book. It has survived not only five centuries, but also the leap into electronic typesetting, remaining essentially unchanged.</p>
<div class="abs btn" style="left:506px;top:967px;width:186px;height:56px">Learn More</div>

<!-- services -->
<section class="abs services"></section>
<div class="abs eyebrow" style="top:1143px">We Provide You</div>
<h2 class="abs section-title" style="top:1170px"><span class="title-mark"></span><span><span class="accent">Our Best</span> Services</span></h2>
<p class="abs lead" style="top:1232px">Red Team Adversary Simulation - A goal based assessment where we attack just like a real world adversary. This includes external attacks and targeted phishing to demonstrate the real risk to your data.</p>

<div class="abs card-photo" style="left:77px;top:1322px;background:linear-gradient(135deg,#2a2a2a,#0d0d0d)" role="img" aria-label="Close-up of a black keyboard with a gold enter key"></div>
<div class="abs card-photo" style="left:622px;top:1322px;background:linear-gradient(135deg,#e9ecef,#8c9aa6)" role="img" aria-label="Laptop showing testing software beside hardware equipment"></div>
<div class="abs card-photo" style="left:77px;top:1691px;background:linear-gradient(135deg,#dfe9f3,#7fa6c8)" role="img" aria-label="Hands holding a smartphone showing charts"></div>
<div class="abs card-photo" style="left:622px;top:1691px;background:linear-gradient(135deg,#0f2438,#3f7cb3)" role="img" aria-label="Analyst seated before a wall of monitors"></div>
<div class="abs card-photo" style="left:77px;top:2062px;background:linear-gradient(135deg,#0c2e4d,#2f7fb8)" role="img" aria-label="Hand touching a glowing network security interface"></div>
<div class="abs card-photo" style="left:622px;top:2062px;background:linear-gradient(135deg,#b7cde0,#4e6a84)" role="img" aria-label="Hooded figure beside a digital padlock graphic"></div>

<div class="abs card-label featured" style="left:115px;top:1540px">Internal Pivot Assessment &amp;<br>Post Exploitation</div>
<div class="abs card-label" style="left:660px;top:1540px">Advanced Product, Hardware &amp;<br>RF Testing</div>
<div class="abs card-label" style="left:115px;top:1911px">Mobile Application<br>Assessment</div>
<div class="abs card-label" style="left:660px;top:1911px">External Penetration<br>Testing</div>
<div class="abs card-label" style="left:115px;top:2282px">Internal Penetration<br>Testing</div>
<div class="abs card-label" style="left:660px;top:2282px">Web Application Penetration<br>Testing</div>

<div class="abs tagline" style="top:2443px">We Are Experienced In Security Consulting And Specifically Offensive Security</div>
<div class="abs btn" style="left:506px;top:2494px;width:186px;height:56px">Contact Us</div>

<!-- testimonials -->
<section class="abs testimonials"></section>
<h2 class="abs section-title" style="top:2660px;color:#fff;left:0"><span class="title-mark" style="background:var(--red-dark)"></span><span>Testimonials</span></h2>
<div class="abs quote-badge" style="left:128px;top:2698px">“</div>
<div class="abs avatar" style="left:182px;top:2706px;background:linear-gradient(160deg,#f2d6c6,#b58d78)" role="img" aria-label="Client portrait"></div>
<p class="abs quote-text" style="color:#fff">" Lorem Ipsum is simply dummy text of the printing and typesetting industry. Lorem Ipsum has been the industry's standard dummy text ever since the 1500s, when an unknown printer took a galley of type and scrambled it to make a type specimen book."</p>
<div class="abs client" style="color:#fff">—Client Name</div>
<svg class="abs" style="left:76px;top:2737px" width="16" height="28" viewBox="0 0 16 28"><path d="M13 2L3 14l10 12" fill="none" stroke="#f6b5b8" stroke-width="2"/></svg>
<svg class="abs" style="left:1106px;top:2737px" width="16" height="28" viewBox="0 0 16 28"><path d="M3 2l10 12L3 26" fill="none" stroke="#f6b5b8" stroke-width="2"/></svg>

<!-- contact -->
<div class="abs contact-photo" style="background:linear-gradient(180deg,#3c3f46,#1d2026)" role="img" aria-label="Man in a striped shirt holding a laptop and pointing forward"></div>
<h2 class="abs section-title" style="top:2943px;left:180px;width:1000px"><span class="title-mark"></span><span><span class="accent">Contact</span> Us</span></h2>
<div class="abs" style="left:494px;top:3006px;width:606px;text-align:center;font-size:17px;color:#444">Need a free quote, or have a question? Get in touch!</div>
<div class="abs field" style="left:494px;top:3054px;width:299px">Name*<svg width="16" height="16" viewBox="0 0 24 24"><circle cx="12" cy="7" r="5" fill="#e8414a"/><path d="M2 23c0-6 4-9 10-9s10 3 10 9z" fill="#e8414a"/></svg></div>
<div class="abs field" style="left:803px;top:3054px;width:297px">Phone*<svg width="16" height="16" viewBox="0 0 24 24"><path fill="#e8414a" d="M6.6 10.8a15.5 15.5 0 0 0 6.6 6.6l2.2-2.2c.3-.3.7-.4 1-.2 1.1.4 2.3.6 3.6.6.6 0 1 .4 1 1V20c0 .6-.4 1-1 1A17 17 0 0 1 3 4c0-.6.4-1 1-1h3.5c.6 0 1 .4 1 1 0 1.3.2 2.5.6 3.6.1.3 0 .7-.2 1z"/></svg></div>
<div class="abs field" style="left:494px;top:3113px;width:606px">Email*<svg width="16" height="14" viewBox="0 0 24 18"><rect width="24" height="18" fill="#e8414a"/><path d="M1 1l11 9 11-9" fill="none" stroke="#fff" stroke-width="2"/></svg></div>
<div class="abs field" style="left:494px;top:3172px;width:606px;height:92px;align-items:flex-start;padding-top:12px">Message*</div>
<div class="abs btn" style="left:721px;top:3277px;width:144px;height:59px">Submit</div>

<!-- call band -->
<section class="abs call-band"></section>
<div class="abs tagline" style="top:3446px;color:#fff">We Are Experienced In Security Consulting And Specifically Offensive Security</div>
<div class="abs" style="left:414px;top:3482px;display:flex;align-items:center;gap:20px;color:#fff;font-size:24px">
  <span>Call Us On :</span>
  <span class="phone-circle"><svg width="34" height="34" viewBox="0 0 24 24"><path fill="#1c1c1c" d="M6.6 10.8a15.5 15.5 0 0 0 6.6 6.6l2.2-2.2c.3-.3.7-.4 1-.2 1.1.4 2.3.6 3.6.6.6 0 1 .4 1 1V20c0 .6-.4 1-1 1A17 17 0 0 1 3 4c0-.6.4-1 1-1h3.5c.6 0 1 .4 1 1 0 1.3.2 2.5.6 3.6.1.3 0 .7-.2 1z"/></svg></span>
  <span>555 - 014 - 2290</span>
</div>

<!-- footer -->
<footer class="abs footer">
  <ul class="footer-nav"><li class="active">Home</li><li>About Us</li><li>Services</li><li>News</li><li>Contact Us</li></ul>
  <div class="social" style="left:978px"></div>
  <div class="social" style="left:1027px"></div>
  <div class="social" style="left:1076px"></div>
  <div class="footer-heading">CONTACT US</div>

  <div class="info-icon" style="left:77px"><svg width="20" height="26" viewBox="0 0 20 26"><path d="M10 0a9 9 0 0 0-9 9c0 7 9 17 9 17s9-10 9-17a9 9 0 0 0-9-9z" fill="#fff"/><circle cx="10" cy="9" r="3.5" fill="#e8414a"/></svg></div>
  <div class="info-text" style="left:150px;top:150px;width:170px">101 - Lorem ipsum is the text simple dummy</div>

  <div class="info-icon" style="left:346px"><svg width="24" height="24" viewBox="0 0 24 24"><path fill="#fff" d="M6.6 10.8a15.5 15.5 0 0 0 6.6 6.6l2.2-2.2c.3-.3.7-.4 1-.2 1.1.4 2.3.6 3.6.6.6 0 1 .4 1 1V20c0 .6-.4 1-1 1A17 17 0 0 1 3 4c0-.6.4-1 1-1h3.5c.6 0 1 .4 1 1 0 1.3.2 2.5.6 3.6.1.3 0 .7-.2 1z"/></svg></div>
  <div class="info-text" style="left:414px;top:163px">555 - 014 - 2290</div>

  <div class="info-icon" style="left:607px"><svg width="24" height="18" viewBox="0 0 24 18"><rect width="24" height="18" fill="#fff"/><path d="M1 1l11 9 11-9" fill="none" stroke="#e8414a" stroke-width="2"/></svg></div>
  <div class="info-text" style="left:678px;top:163px">hello@blueharbor-sec.com</div>

  <div class="info-text" style="left:872px;top:163px;font-size:13px">©BLUEHARBOR - 2017 All Right Reserved.</div>
</footer>

</body>
</html>
```